K7 Digital Stationery Design Project

We are looking to have stationary designs created for our company branding materials. We are looking for the following to be created.
1. Business Cards (front & back)
2. Letterhead
3. Envelopes #10
We are a new web design, development and marketing firm. Primary color scheme is desired to be blue/grey/white. This web start-up is owned and operated by individuals with 15+ years experience each in the industry so should not look as though it is a start-up by young/inexperienced individuals.
We build website & custom applications/software. In addition we provide the full spectrum of web marketing solutions including SEO, PPC, Social Media, Branding, Content Marketing and PR.
Please let us know if you have any questions. Looking forward to seeing all the amazing design ideas.
Attached is our logo.
Thanks!
Target Market(s)
Company will be nearly 100% business to business sales. Looking to work with companies that are already established, with a website, who want to take their website and/or online marketing efforts to the next level.
Industry/Entity Type
Marketing
Look and feel

```html
<!DOCTYPE html>
<html lang="en">
<head>
<meta charset="utf-8">
<title>K7 Digital Stationery</title>
<link rel="stylesheet" href="https://fonts.googleapis.com/css2?family=Didact+Gothic&display=swap">
<style>
  :root {
    --blue: #2f6fd6;
    --blue-deep: #1f4fa8;
    --blue-light: #5aa0f0;
    --ink: #1a1a1a;
    --grey: #6b6b6b;
    --paper: #ffffff;
    --edge: #9a9a9a;
    --card: #050505;
  }
  * { margin: 0; padding: 0; box-sizing: border-box; }
  html, body { width: 1200px; height: 2200px; overflow: hidden; }
  body {
    background: var(--paper);
    font-family: "Didact Gothic", "Century Gothic", sans-serif;
    color: var(--ink);
    position: relative;
  }
  .sheet {
    position: absolute;
    background: var(--paper);
    border: 2px solid var(--edge);
    box-shadow: 2px 3px 6px rgba(0,0,0,.12);
  }
  .letterhead--back { left: 410px; top: 96px; width: 660px; height: 860px; transform: rotate(3deg); }
  .letterhead--front { left: 130px; top: 84px; width: 720px; height: 990px; }

  .brand { display: flex; align-items: center; gap: 12px; }
  .brand__dot { width: 34px; height: 34px; border-radius: 50%; background: var(--blue); flex: none; }
  .brand__name { font-size: 38px; letter-spacing: 1px; color: var(--ink); line-height: 1; }
  .brand__tag { font-size: 15px; color: var(--ink); margin-top: 4px; }

  .footer-band {
    position: absolute; left: 0; right: 0; height: 26px;
    background: linear-gradient(90deg, var(--blue-deep), var(--blue), var(--blue-light));
    color: #fff; font-size: 12px; display: flex; align-items: center; justify-content: flex-end;
    padding-right: 18px; letter-spacing: .3px;
  }
  .letterhead--back .footer-band { bottom: 100px; }
  .letterhead--back .footer-band span { opacity: .9; }
  .letterhead--front .brand-block { position: absolute; left: 22px; bottom: 74px; }
  .letterhead--front .footer-band { bottom: 40px; }

  .envelope { left: 208px; top: 1180px; width: 784px; height: 340px; border: 3px solid var(--ink); box-shadow: none; }
  .envelope .brand-block { position: absolute; left: 26px; top: 22px; }
  .envelope .brand__name { font-size: 28px; }
  .envelope .brand__dot { width: 26px; height: 26px; }
  .envelope .brand__tag { font-size: 11px; }
  .envelope .return { font-size: 14px; line-height: 1.35; margin: 6px 0 0 38px; }
  .envelope .return-band {
    margin: 6px 0 0 0; height: 16px; width: 200px;
    background: linear-gradient(90deg, var(--blue-deep), var(--blue-light));
    color: #fff; font-size: 10px; padding-left: 60px; line-height: 16px;
  }

  .card {
    position: absolute; background: var(--card); color: #fff; overflow: hidden;
    box-shadow: 3px 4px 8px rgba(0,0,0,.3);
  }
  .card--contact { left: 208px; top: 1600px; width: 560px; height: 320px; transform: rotate(-1deg); }
  .card--contact .accent-bar {
    position: absolute; left: 0; top: 210px; width: 100%; height: 30px;
    background: linear-gradient(90deg, var(--blue-deep), var(--blue), rgba(47,111,214,.25));
  }
  .card--contact .accent-shape {
    position: absolute; left: 22px; top: 30px; width: 120px; height: 260px;
    background: linear-gradient(160deg, var(--blue-light), var(--blue-deep));
    border-radius: 60px 60px 60px 60px; opacity: .9;
  }
  .card--contact .details { position: absolute; left: 190px; top: 36px; font-size: 15px; line-height: 1.35; }
  .card--contact .person { font-size: 22px; letter-spacing: .5px; }
  .card--contact .title { font-size: 14px; color: #d8d8d8; margin-bottom: 14px; }
  .card--contact .gap { height: 12px; }

  .card--brand { left: 570px; top: 1738px; width: 510px; height: 330px; transform: rotate(-3deg); }
  .card--brand .brand-block { position: absolute; right: 28px; bottom: 36px; text-align: left; }
  .card--brand .brand__name { color: #fff; font-size: 34px; }
  .card--brand .brand__tag { color: #fff; font-size: 14px; }
  .card--brand .brand__dot { width: 30px; height: 30px; }
</style>
</head>
<body>

  <section class="sheet letterhead--back" aria-label="Letterhead, second page">
    <div class="footer-band"><span>00 Somewhere Street, City, State, Zip | 000.000.0000 | www.k7digital.com</span></div>
  </section>

  <section class="sheet letterhead--front" aria-label="Letterhead">
    <div class="brand-block">
      <div class="brand"><span class="brand__dot"></span><span class="brand__name">K7 DIGITAL</span></div>
      <p class="brand__tag" style="margin-left:46px">Web Design, Development and Marketing</p>
    </div>
    <div class="footer-band">00 Somewhere Street, City, State, Zip | T: 000.000.0000 | F: 000.000.0000 | www.k7digital.com</div>
  </section>

  <section class="sheet envelope" aria-label="Envelope #10">
    <div class="brand-block">
      <div class="brand"><span class="brand__dot"></span><span class="brand__name">K7 DIGITAL</span></div>
      <p class="brand__tag" style="margin-left:38px">Web Design, Development and Marketing</p>
      <p class="return">00 Somewhere Street<br>City, State, Zip</p>
      <div class="return-band">www.k7digital.com</div>
    </div>
  </section>

  <section class="card card--contact" aria-label="Business card, contact side">
    <div class="accent-shape" role="img" aria-label="Blue gradient decorative shape"></div>
    <div class="accent-bar"></div>
    <div class="details">
      <p class="person">FIRST LAST NAME</p>
      <p class="title">Title</p>
      <p>00 Somewhere Street<br>City, State, Zip</p>
      <div class="gap"></div>
      <p>hello@k7digital.com</p>
      <div class="gap"></div>
      <p>000.000.0000 | 000.000.0000</p>
      <p>www.k7digital.com</p>
    </div>
  </section>

  <section class="card card--brand" aria-label="Business card, brand side">
    <div class="brand-block">
      <div class="brand"><span class="brand__dot"></span><span class="brand__name">K7 DIGITAL</span></div>
      <p class="brand__tag">Web Design, Development and Marketing</p>
    </div>
  </section>

</body>
</html>
```